Yard Sign Design Needed

Yard sign needed for mowing & landscaping company. Would like to use the top logo with black background which is attached. Would like MOWING to be in large standout letters. The word "landscaping" can be smaller and more artistic or omitted. Will need room for phone number once design is approved. The phone number will need to stand out and look identical/similar to the word 'MOWING"

```html
<!DOCTYPE html>
<html lang="en">
<head>
<meta charset="utf-8">
<title>Mowing Landscaping Yard Sign</title>
<link rel="stylesheet" href="https://fonts.googleapis.com/css2?family=Montserrat:wght@600;800&family=Dancing+Script:wght@600&display=swap">
<style>
  :root {
    --sign-black: #000000;
    --lime: #aaed45;
    --white: #ffffff;
    --backdrop: #e8ebe4;
  }
  * { margin: 0; padding: 0; box-sizing: border-box; }
  html, body { width: 1200px; height: 990px; overflow: hidden; background: var(--backdrop); }
  .canvas { position: relative; width: 1200px; height: 990px; }

  .sign { position: absolute; background: var(--sign-black); overflow: hidden; }
  .sign-main { left: 40px; top: 30px; width: 980px; height: 700px; }

  .headline {
    position: absolute; left: 0; right: 0; text-align: center;
    font-family: "Montserrat", sans-serif; font-weight: 800; color: var(--lime);
    line-height: 1; white-space: nowrap;
  }
  .tagline {
    position: absolute; left: 0; right: 0; text-align: center;
    font-family: "Dancing Script", cursive; font-weight: 600; color: var(--white);
    line-height: 1; white-space: nowrap;
  }
  .bracket { position: absolute; left: 0; top: 0; }
  .company { position: absolute; left: 0; right: 0; display: flex; flex-direction: column; align-items: center; }
  .company-mark { background: var(--lime); }
  .company-name {
    font-family: "Montserrat", sans-serif; font-weight: 600; color: var(--white);
    text-align: center; line-height: 1.15; white-space: nowrap;
  }
  .phone {
    position: absolute; left: 0; right: 0; text-align: center;
    font-family: "Montserrat", sans-serif; font-weight: 800; color: var(--white);
    line-height: 1; white-space: nowrap;
  }

  /* main sign */
  .sign-main .headline { top: 78px; font-size: 172px; letter-spacing: -4px; }
  .sign-main .tagline { top: 248px; font-size: 66px; }
  .sign-main .company { top: 372px; gap: 14px; }
  .sign-main .company-mark { width: 52px; height: 52px; }
  .sign-main .company-name { font-size: 20px; letter-spacing: 1px; }
  .sign-main .phone { top: 488px; font-size: 132px; letter-spacing: -6px; }

  /* small variants */
  .sign-mini { width: 270px; height: 180px; top: 775px; }
  .sign-mini.white-band { left: 620px; }
  .sign-mini.lime-band { left: 910px; top: 773px; }
  .sign-mini .headline { top: 16px; font-size: 46px; letter-spacing: -1px; }
  .sign-mini .tagline { top: 60px; font-size: 17px; }
  .sign-mini .company { top: 86px; gap: 3px; }
  .sign-mini .company-mark { width: 14px; height: 14px; }
  .sign-mini .company-name { font-size: 5px; }
  .phone-band {
    position: absolute; left: 0; right: 0; bottom: 0; height: 44px;
    display: flex; align-items: center; justify-content: center;
    font-family: "Montserrat", sans-serif; font-weight: 800; font-size: 33px;
    letter-spacing: -1.5px; color: var(--sign-black); white-space: nowrap;
  }
  .white-band .phone-band { background: var(--white); }
  .lime-band .phone-band { background: var(--lime); }
</style>
</head>
<body>
<main class="canvas">

  <section class="sign sign-main">
    <svg class="bracket" width="980" height="700" viewBox="0 0 980 700" aria-hidden="true">
      <g fill="none" stroke="var(--lime)" stroke-width="5">
        <polyline points="100,158 62,158 62,318 340,318"/>
        <polyline points="880,158 918,158 918,312 735,312"/>
      </g>
    </svg>
    <h1 class="headline">MOWING</h1>
    <p class="tagline">Landscaping</p>
    <div class="company">
      <span class="company-mark"></span>
      <span class="company-name">NORVAN CONTRACTORS LLC</span>
    </div>
    <p class="phone">555-208-7461</p>
  </section>

  <section class="sign sign-mini white-band">
    <svg class="bracket" width="270" height="180" viewBox="0 0 270 180" aria-hidden="true">
      <g fill="none" stroke="var(--lime)" stroke-width="2">
        <polyline points="22,36 12,36 12,72 82,72"/>
        <polyline points="248,36 258,36 258,70 190,70"/>
      </g>
    </svg>
    <h2 class="headline">MOWING</h2>
    <p class="tagline">Landscaping</p>
    <div class="company">
      <span class="company-mark"></span>
      <span class="company-name">NORVAN CONTRACTORS LLC</span>
    </div>
    <p class="phone-band">555-208-7461</p>
  </section>

  <section class="sign sign-mini lime-band">
    <svg class="bracket" width="270" height="180" viewBox="0 0 270 180" aria-hidden="true">
      <g fill="none" stroke="var(--lime)" stroke-width="2">
        <polyline points="22,36 12,36 12,72 82,72"/>
        <polyline points="248,36 258,36 258,70 190,70"/>
      </g>
    </svg>
    <h2 class="headline">MOWING</h2>
    <p class="tagline">Landscaping</p>
    <div class="company">
      <span class="company-mark"></span>
      <span class="company-name">NORVAN CONTRACTORS LLC</span>
    </div>
    <p class="phone-band">555-208-7461</p>
  </section>

</main>
</body>
</html>
```